Marlow Hire Business Card for recruitment company

We are looking for a Business Card Design that incorporates our personal details and our busines name and logo. We are a specialized search consultancy that recruit Property and Construction professionals.
We would like a business card that stands out and is appealing to the Construction and Property industry as well.

Target Market(s)

people in the construction and property industry

Contact Information for Business Card

Business Name and logo

Font styles to use
Serif

Colors
0094D4
00A9DD
6FCCEA
C7EBF8
E9F6FB

Requirements
Must have
• Business name and logo as well as contact details
Should not have
• No photos of us please

```html
<!DOCTYPE html>
<html lang="en">
<head>
<meta charset="utf-8">
<title>Marlow Hire – Business Card</title>
<link rel="stylesheet" href="https://fonts.googleapis.com/css2?family=Montserrat:wght@400;500;700&display=swap">
<style>
  :root {
    --page: #ffffff;
    --card-light: #eeeeee;
    --navy: #003446;
    --navy-text: #0b3f52;
    --white: #ffffff;
  }
  * { margin: 0; padding: 0; box-sizing: border-box; }
  html, body {
    width: 900px;
    height: 1200px;
    overflow: hidden;
    background: var(--page);
    font-family: "Montserrat", sans-serif;
  }
  .sheet {
    position: relative;
    width: 900px;
    height: 1200px;
  }
  .card {
    position: absolute;
    left: 66px;
    width: 768px;
    height: 469px;
    text-align: center;
  }
  .card--front {
    top: 81px;
    background: var(--card-light);
    color: var(--navy-text);
  }
  .card--back {
    top: 650px;
    background: var(--navy);
    color: var(--white);
  }
  .wordmark {
    position: absolute;
    left: 0;
    right: 0;
    font-weight: 400;
    text-transform: uppercase;
    letter-spacing: 0.02em;
    line-height: 1;
  }
  .card--front .wordmark {
    top: 28px;
    font-size: 40px;
    color: var(--navy);
  }
  .card--back .wordmark {
    top: 218px;
    font-size: 50px;
  }
  .identity {
    position: absolute;
    left: 0;
    right: 0;
    top: 202px;
  }
  .identity__name {
    font-size: 31px;
    font-weight: 700;
    color: var(--navy);
    line-height: 1.2;
  }
  .identity__role {
    margin-top: 4px;
    font-size: 18px;
    font-weight: 400;
    letter-spacing: 0.3em;
    padding-left: 0.3em;
  }
  .contact {
    position: absolute;
    left: 0;
    right: 0;
    top: 367px;
    font-size: 17px;
    line-height: 24px;
  }
  .contact__phone {
    letter-spacing: 0.3em;
    padding-left: 0.3em;
  }
  .contact__web {
    margin-top: 5px;
    font-weight: 700;
    color: var(--navy);
  }
</style>
</head>
<body>
  <main class="sheet">
    <section class="card card--front" aria-label="Card front">
      <div class="wordmark">Marlow Hire</div>
      <div class="identity">
        <h1 class="identity__name">Your Name</h1>
        <p class="identity__role">Your Position</p>
      </div>
      <div class="contact">
        <p class="contact__phone">+64-27-480-2291</p>
        <p class="contact__email">ines@marlowhire.nz</p>
        <p class="contact__web">marlowhire.nz</p>
      </div>
    </section>

    <section class="card card--back" aria-label="Card back">
      <div class="wordmark">Marlow Hire</div>
    </section>
  </main>
</body>
</html>
```